Childcare Centre Franchise Website Design

Our business is Childcare centre, and we are the franchise with 4 centres currently, we would like to have the website similar as the link below,
https://www.brambleoak.edu.au/
with the same items, functions and pages. Locations information for all centres, and have pages for each centre. Additionally, we will need a page for online enrolment.
Our logo is attached.

```html
<!DOCTYPE html>
<html lang="en">
<head>
<meta charset="utf-8">
<title>Little Meadow Childcare</title>
<link rel="stylesheet" href="https://fonts.googleapis.com/css2?family=Playfair+Display:wght@600;700&family=Poppins:wght@400;500;600&display=swap">
<style>
:root{
  --pink:#d6447e;
  --pink-soft:#f6d3e1;
  --green:#8dc63f;
  --lime:#d5e64a;
  --teal:#1fa596;
  --brown:#7b3f2b;
  --ink:#3a2a24;
  --heading:#5a2a1c;
  --hero-title:#3f6b2a;
  --muted:#7a6e69;
  --card:#ffffff;
  --bg:#ffffff;
}
*{box-sizing:border-box;margin:0;padding:0}
html,body{width:1200px;height:4220px;overflow:hidden}
body{position:relative;background:var(--bg);font-family:'Poppins',sans-serif;color:var(--ink)}
.abs{position:absolute}
.h-serif{font-family:'Playfair Display',serif;color:var(--heading);font-weight:700}
.ph{display:block}

/* header */
.site-header{left:0;top:0;width:1200px;height:80px}
.brand{left:18px;top:14px;display:flex;align-items:center;gap:8px;font-weight:600;font-size:15px;color:var(--pink)}
.brand-dot{width:16px;height:16px;border-radius:50%;background:var(--green)}
.main-nav{left:370px;top:30px;display:flex;gap:26px;font-size:14px;font-weight:500;color:var(--ink);white-space:nowrap}
.main-nav .home{color:var(--pink)}
.search-btn{left:1000px;top:20px;width:110px;height:40px;border-radius:20px;background:var(--pink);color:#fff;font-size:14px;font-weight:500;display:flex;align-items:center;justify-content:center}

/* hero */
.hero-photo{left:0;top:80px;width:1200px;height:820px}
.hero-blob{left:0;top:150px;width:560px;height:520px}
.hero-title{left:150px;top:330px;width:420px;font-family:'Playfair Display',serif;font-weight:700;font-size:46px;line-height:1.15;color:var(--hero-title)}
.enroll{left:140px;top:570px;width:110px;height:110px;border-radius:50%;background:var(--pink);color:#fff;font-size:15px;font-weight:600;display:flex;align-items:center;justify-content:center;text-align:center;line-height:1.2;transform:rotate(-14deg)}

/* about */
.about-photo{left:100px;top:880px;width:430px;height:470px}
.about-text{left:690px;top:1040px;width:420px}
.about-text h2{font-size:44px;margin-bottom:18px}
.about-text p{font-size:13.5px;line-height:1.6;color:var(--muted);margin-bottom:12px}
.btn-pink{display:inline-flex;align-items:center;justify-content:center;background:var(--pink);color:#fff;font-size:13px;font-weight:500;border-radius:22px;height:42px;padding:0 26px}

/* support */
.section-title{width:1200px;left:0;text-align:center;font-size:40px}
.section-sub{width:1200px;left:0;text-align:center;font-size:17px;font-weight:600;color:var(--ink)}
.support-item{width:200px;height:200px}
.support-item .support-blob{position:absolute;left:0;top:0}
.support-label{position:absolute;left:0;top:95px;width:200px;text-align:center;font-family:'Playfair Display',serif;font-weight:700;font-size:18px;color:#fff;line-height:1.2}
.support-item .support-icon{position:absolute;left:82px;top:45px}

/* learning */
.learn-card{width:232px;height:265px;background:var(--card);border-radius:14px;box-shadow:0 6px 20px rgba(0,0,0,.12);padding:16px 14px}
.learn-card h3{font-family:'Playfair Display',serif;font-size:17px;color:var(--heading);line-height:1.2;height:50px}
.learn-card .ph{width:204px;height:170px;border-radius:10px;margin-top:8px}
.btn-outline{left:490px;top:2320px;width:220px;height:44px;border:1.5px solid #bfb3ad;border-radius:22px;font-size:13px;display:flex;align-items:center;justify-content:center;color:var(--ink)}

/* village */
.centre{width:320px;height:120px;display:flex;gap:18px}
.centre .ph{width:115px;height:115px;border-radius:12px;flex:none}
.centre h4{font-family:'Playfair Display',serif;font-size:17px;color:var(--heading);line-height:1.25;margin-top:14px}
.centre span{display:block;margin-top:8px;font-size:12px;color:var(--muted)}

/* blog */
.blog-head{left:200px;top:3210px}
.blog-head h2{font-size:46px;line-height:1.1;margin-bottom:24px}
.blog-card{width:310px;height:430px;background:var(--card);border-radius:14px;box-shadow:0 6px 22px rgba(0,0,0,.12);padding:22px 22px}
.blog-card small{font-size:12px;color:var(--muted);letter-spacing:1px}
.blog-card h3{font-family:'Playfair Display',serif;font-size:20px;color:var(--heading);line-height:1.25;margin:8px 0 16px}
.blog-card .ph{width:266px;height:290px;border-radius:10px}

/* trial + footer */
.footer-bg{left:0;top:3600px;width:1200px;height:620px;background:var(--brown)}
.trial{left:140px;top:3480px;width:920px;height:220px}
.trial-title{left:250px;top:3565px;font-family:'Playfair Display',serif;font-weight:700;font-size:36px;color:#fff}
.trial-btn{left:860px;top:3562px;width:150px;height:46px;border-radius:23px;background:#fff;color:var(--pink);font-size:14px;font-weight:600;display:flex;align-items:center;justify-content:center}
.foot-col h5{font-size:15px;font-weight:600;color:#fff;letter-spacing:1px;margin-bottom:18px}
.foot-col li{list-style:none;font-size:13px;color:#f1dcd3;margin-bottom:10px}
.foot-col li::before{content:"›";margin-right:8px;color:var(--pink-soft)}
.contact-row{display:flex;gap:12px;margin-bottom:16px;font-size:13px;color:#f1dcd3;line-height:1.45}
.news-input{margin-top:18px;width:260px;height:42px;border-radius:21px;background:#fff;display:flex;align-items:center;justify-content:space-between;padding:0 8px 0 18px;font-size:12px;color:var(--muted)}
.foot-rule{left:0;top:4150px;width:1200px;height:1px;background:rgba(255,255,255,.2)}
.copyright{left:0;top:4172px;width:1200px;text-align:center;font-size:13px;color:#f1dcd3}
.to-top{left:1130px;top:4160px;width:40px;height:40px;border-radius:50%;background:var(--pink);display:flex;align-items:center;justify-content:center}
</style>
</head>
<body>

<header class="abs site-header">
  <div class="abs brand"><span class="brand-dot"></span>Little Meadow</div>
  <nav class="abs main-nav">
    <span class="home">&#8962;</span><span>About Us</span><span>Education</span><span>Centres</span><span>Subsidy</span><span>News &amp; Advice</span><span>Careers</span>
  </nav>
  <div class="abs search-btn">Search</div>
</header>

<svg class="abs hero-photo" viewBox="0 0 1200 820" role="img" aria-label="Photo of a smiling mother and daughter playing together at a table with coloured eggs">
  <defs>
    <linearGradient id="heroGrad" x1="0" y1="0" x2="1" y2="1">
      <stop offset="0" stop-color="#efe4d2"/><stop offset=".55" stop-color="#e8c8a8"/><stop offset="1" stop-color="#c99a7c"/>
    </linearGradient>
  </defs>
  <path d="M0 0H1200V650C1050 610 900 700 760 720 560 750 420 690 250 740 150 770 60 760 0 740Z" fill="url(#heroGrad)"/>
  <path d="M0 740C80 770 170 760 260 735 420 690 560 760 760 730 900 710 1050 620 1200 660V720C1050 690 930 780 760 795 560 815 420 760 260 800 160 825 70 820 0 800Z" fill="var(--lime)"/>
  <path d="M430 760C600 745 700 800 900 760 1000 740 1100 700 1200 710V745C1100 745 1000 790 880 805 700 825 560 790 430 790Z" fill="var(--green)"/>
</svg>
<svg class="abs hero-blob" viewBox="0 0 560 520" aria-hidden="true">
  <path d="M60 160C90 70 220 40 340 60 460 80 540 150 520 270 500 380 400 430 280 440 160 450 70 420 50 330 40 270 40 220 60 160Z" fill="#fff"/>
</svg>
<h1 class="abs hero-title">Little Meadow Creating a world Of Wonde</h1>
<div class="abs enroll">ENROLL<br>NOW</div>

<svg class="abs about-photo" viewBox="0 0 430 470" role="img" aria-label="Photo of two toddlers playing on a small purple slide">
  <path d="M20 220C20 90 120 10 230 20 350 30 420 130 415 250 410 380 320 460 210 455 100 450 20 360 20 220Z" fill="var(--pink)"/>
  <path d="M40 225C40 105 130 35 230 42 340 50 398 140 393 250 388 365 305 435 210 430 110 425 40 345 40 225Z" fill="#cbb8b0"/>
  <path d="M170 250h150v120H170z" fill="#a06ac4" opacity=".55"/>
</svg>
<div class="abs about-text">
  <h2 class="h-serif">About Chileare</h2>
  <p>Little Meadow is much more than a place of childcare and learning. It is a place where children feel safe and secure to be themselves, a place where children can be curious, imaginative and brave in their learning. We create an environment that supports children with the best possible start to life.</p>
  <p>We believe that if we focus our enormous passion on the care and education of young children, then these children will thrive.</p>
  <span class="btn-pink" style="margin-top:14px">Read more</span>
</div>

<h2 class="abs section-title h-serif" style="top:1550px">We're here to Support the Whole Family</h2>
<div class="abs support-item" style="left:225px;top:1650px">
  <svg class="support-blob" width="200" height="200" viewBox="0 0 200 200" aria-hidden="true"><path d="M30 60C60 10 160 10 185 70 205 130 160 195 90 190 30 185 0 120 30 60Z" fill="var(--green)"/></svg>
  <svg class="support-icon" width="36" height="36" viewBox="0 0 36 36" aria-hidden="true"><circle cx="18" cy="18" r="16" fill="none" stroke="#fff" stroke-width="2"/><path d="M11 18l5 5 9-10" fill="none" stroke="#fff" stroke-width="2"/></svg>
  <div class="support-label">Child Care<br>Subsidy</div>
</div>
<div class="abs support-item" style="left:505px;top:1640px">
  <svg class="support-blob" width="200" height="200" viewBox="0 0 200 200" aria-hidden="true"><path d="M40 40C90 0 175 20 190 90 200 160 140 200 80 190 20 180 -5 80 40 40Z" fill="var(--pink)"/></svg>
  <svg class="support-icon" width="36" height="36" viewBox="0 0 36 36" aria-hidden="true"><path d="M18 31S4 22 4 12a7 7 0 0 1 14-2 7 7 0 0 1 14 2c0 10-14 19-14 19z" fill="none" stroke="#fff" stroke-width="2"/></svg>
  <div class="support-label">Why Little<br>Meadow</div>
</div>
<div class="abs support-item" style="left:785px;top:1650px">
  <svg class="support-blob" width="200" height="200" viewBox="0 0 200 200" aria-hidden="true"><path d="M25 90C20 30 100 0 160 30 210 60 200 150 140 185 80 210 30 150 25 90Z" fill="var(--teal)"/></svg>
  <svg class="support-icon" width="36" height="36" viewBox="0 0 36 36" aria-hidden="true"><path d="M18 4v28M4 18h28" stroke="#fff" stroke-width="3"/><circle cx="18" cy="18" r="15" fill="none" stroke="#fff" stroke-width="2"/></svg>
  <div class="support-label">Health And<br>Wellbeing</div>
</div>

<h2 class="abs section-title h-serif" style="top:1930px">A love of Learning</h2>
<p class="abs section-sub" style="top:1985px">Confidence. Curiosity. Here are some of the ways we help children thrive.</p>
<div class="abs learn-card" style="left:140px;top:2035px"><h3>High-Quality Curriculum</h3><div class="ph" role="img" aria-label="Photo of a child drawing at a classroom table" style="background:linear-gradient(135deg,#e9d9c8,#b9c7a2)"></div></div>
<div class="abs learn-card" style="left:373px;top:2035px"><h3>Exciting Environments</h3><div class="ph" role="img" aria-label="Photo of children playing together in a bright play room" style="background:linear-gradient(135deg,#f0cfa7,#d28f6f)"></div></div>
<div class="abs learn-card" style="left:606px;top:2035px"><h3>Wellbeing And Nutrition</h3><div class="ph" role="img" aria-label="Photo of children sharing a healthy snack" style="background:linear-gradient(135deg,#f2e0c6,#e0a46c)"></div></div>
<div class="abs learn-card" style="left:839px;top:2035px"><h3>Community Connections</h3><div class="ph" role="img" aria-label="Photo of children building with colourful blocks" style="background:linear-gradient(135deg,#f4c66a,#d96a4e)"></div></div>
<div class="abs btn-outline">Discover our Approach</div>

<h2 class="abs section-title h-serif" style="top:2425px">Find your Village</h2>
<p class="abs section-sub" style="top:2480px">Childcare Centres by State</p>

<div class="abs centre" style="left:80px;top:2530px"><div class="ph" role="img" aria-label="Photo of children at a childcare centre" style="background:linear-gradient(135deg,#c9dbe8,#e7b48a)"></div><div><h4>Bramble Oak Childcare &amp; Education Croydon Park</h4><span>Read more ›</span></div></div>
<div class="abs centre" style="left:470px;top:2530px"><div class="ph" role="img" aria-label="Photo of children at a childcare centre" style="background:linear-gradient(135deg,#d8e6b9,#e6a77b)"></div><div><h4>Bramble Oak Childcare &amp; Education Croydon Park</h4><span>Read more ›</span></div></div>
<div class="abs centre" style="left:860px;top:2530px"><div class="ph" role="img" aria-label="Photo of children at a childcare centre" style="background:linear-gradient(135deg,#f1d6b5,#cf8a6a)"></div><div><h4>Bramble Oak Childcare &amp; Education Croydon Park</h4><span>Read more ›</span></div></div>

<div class="abs centre" style="left:80px;top:2660px"><div class="ph" role="img" aria-label="Photo of children at a childcare centre" style="background:linear-gradient(135deg,#f0c7a0,#b7cfa1)"></div><div><h4>Bramble Oak Childcare &amp; Education Croydon Park</h4><span>Read more ›</span></div></div>
<div class="abs centre" style="left:470px;top:2660px"><div class="ph" role="img" aria-label="Photo of children at a childcare centre" style="background:linear-gradient(135deg,#f3d9a8,#d47a68)"></div><div><h4>Bramble Oak Childcare &amp; Education Croydon Park</h4><span>Read more ›</span></div></div>
<div class="abs centre" style="left:860px;top:2660px"><div class="ph" role="img" aria-label="Photo of children at a childcare centre" style="background:linear-gradient(135deg,#e8b6c4,#f2d39c)"></div><div><h4>Bramble Oak Childcare &amp; Education Croydon Park</h4><span>Read more ›</span></div></div>

<div class="abs centre" style="left:80px;top:2790px"><div class="ph" role="img" aria-label="Photo of children at a childcare centre" style="background:linear-gradient(135deg,#c8d9a9,#e9c28a)"></div><div><h4>Bramble Oak Childcare &amp; Education Croydon Park</h4><span>Read more ›</span></div></div>
<div class="abs centre" style="left:470px;top:2790px"><div class="ph" role="img" aria-label="Photo of children at a childcare centre" style="background:linear-gradient(135deg,#f0cc9e,#a9c3d4)"></div><div><h4>Bramble Oak Childcare &amp; Education Croydon Park</h4><span>Read more ›</span></div></div>
<div class="abs centre" style="left:860px;top:2790px"><div class="ph" role="img" aria-label="Photo of children at a childcare centre" style="background:linear-gradient(135deg,#f4d0a4,#e39073)"></div><div><h4>Bramble Oak Childcare &amp; Education Croydon Park</h4><span>Read more ›</span></div></div>

<div class="abs blog-head">
  <h2 class="h-serif">Our Letest<br>Blog</h2>
  <span class="btn-pink">View All Blogs</span>
</div>
<div class="abs blog-card" style="left:450px;top:3020px"><small>WEEKS</small><h3>10 signs your child might be ready for school</h3><div class="ph" role="img" aria-label="Photo of a toddler stacking colourful toy blocks" style="background:linear-gradient(135deg,#dfe8f0,#f0b96a)"></div></div>
<div class="abs blog-card" style="left:760px;top:3000px"><small>WEEKS</small><h3>10 signs your child might be ready for school</h3><div class="ph" role="img" aria-label="Photo of two children playing with bright toys" style="background:linear-gradient(135deg,#bcd6ea,#e78d6c)"></div></div>

<div class="abs footer-bg"></div>
<svg class="abs trial" viewBox="0 0 920 220" aria-hidden="true">
  <path d="M110 10H810C870 10 915 55 915 110 915 165 870 210 810 210H110C50 210 5 165 5 110 5 55 50 10 110 10Z" fill="var(--pink)"/>
</svg>
<div class="abs trial-title">Book A Trial Lesson</div>
<div class="abs trial-btn">Try For Free</div>

<div class="abs foot-col" style="left:160px;top:3860px">
  <h5>INFORMATION</h5>
  <ul><li>Find Your Closest Centre</li><li>Childcare NSW</li><li>Childcare VIC</li><li>Childcare QLD</li><li>Childcare ACT</li><li>Childcare SA</li></ul>
</div>
<div class="abs foot-col" style="left:390px;top:3860px">
  <h5>QUICK LINKS</h5>
  <ul><li>Home</li><li>About Us</li><li>Education</li><li>Centres</li><li>Subsidy</li><li>News &amp; Advice</li><li>Careers</li></ul>
</div>
<div class="abs foot-col" style="left:575px;top:3860px;width:220px">
  <h5>CONTACT INFO</h5>
  <div class="contact-row"><svg width="16" height="16" viewBox="0 0 16 16" aria-hidden="true"><rect x="1" y="3" width="14" height="10" rx="1" fill="none" stroke="#f6d3e1" stroke-width="1.4"/><path d="M1 4l7 5 7-5" fill="none" stroke="#f6d3e1" stroke-width="1.4"/></svg><div>Email<br>hello@littlemeadow.example</div></div>
  <div class="contact-row"><svg width="16" height="16" viewBox="0 0 16 16" aria-hidden="true"><path d="M4 1l3 3-2 2c1 2 3 4 5 5l2-2 3 3-2 3C7 15 1 9 1 3z" fill="#f6d3e1"/></svg><div>Phone<br>+61 2 5550 0148</div></div>
  <div class="contact-row"><svg width="16" height="16" viewBox="0 0 16 16" aria-hidden="true"><path d="M8 15S2 9 2 6a6 6 0 0 1 12 0c0 3-6 9-6 9z" fill="#f6d3e1"/><circle cx="8" cy="6" r="2" fill="var(--brown)"/></svg><div>Location<br>12 Wattle Lane,<br>Ashfield NSW 2131</div></div>
</div>
<div class="abs foot-col" style="left:820px;top:3860px;width:280px">
  <h5>NEWSLETTER</h5>
  <p style="font-size:13px;color:#f1dcd3;line-height:1.5">Subscribe to our email address to get the latest news.</p>
  <div class="news-input">Enter your email...<svg width="26" height="26" viewBox="0 0 26 26" aria-hidden="true"><circle cx="13" cy="13" r="13" fill="var(--pink)"/><path d="M7 13h11M14 9l4 4-4 4" fill="none" stroke="#fff" stroke-width="1.8"/></svg></div>
</div>
<div class="abs foot-rule"></div>
<div class="abs copyright">© Copyright 2021. All Rights Reserved</div>
<div class="abs to-top"><svg width="14" height="14" viewBox="0 0 14 14" aria-hidden="true"><path d="M2 9l5-5 5 5" fill="none" stroke="#fff" stroke-width="2"/></svg></div>

</body>
</html>
```